Darrow Consulting needs a quality & professional business card!

I am a recruitment and employment consultant from Brisbane, Australia and I had a fantastic logo organised by this community to I am hoping the business card will be the same.

I have attached the Darrow consulting logo that ideally would feature on the back of the business card. There are a number of logos for you to use as you see fit. I would like the colour cheme to match that of the Darrow Consulting logo. I also have a secondary company called Career Lantern Australia and I have included that logo as well. While it is an important part of the business I don't want this logo feature too predominantly as I am moving out of this space. This logo was created by myself and is of low quality. Feel free to use the icon and words however you want. The winning design will be smart, professional and eye-catching.

The information I am looking for in the business card is:
Name: Gavin Darrow
Position: Founder & Director
Phone: (07) 3519 6482
Mobile: 0431 586 207
Email: gavin@careerlantern.com.au

Target Market(s)

Recruiters, government, large companies

Contact Information for Business Card

Name: Gavin Darrow
Phone: (07) 3519 6482
Mobile: 0431 586 207
Web: www.careerlantern.com.au

Font styles to use
Serif
Sans Serif

Requirements
Must have
• Darrow Consulting Logo on reverse side
• Contact details on front side with smaller reference to Darrow Consulting logo and Career Lantern Australia logo

```html
<!DOCTYPE html>
<html lang="en">
<head>
<meta charset="utf-8">
<title>Darrow Consulting – Business Card</title>
<link rel="stylesheet" href="https://fonts.googleapis.com/css2?family=Arimo:wght@400;700&display=swap">
<style>
  :root {
    --backdrop: #2a2a2b;
    --card-dark: #25272a;
    --band-light: #ffffff;
    --band-shade: #dcdcdc;
    --ink-dark: #2b2b2b;
    --ink-light: #c9cbcd;
    --ink-muted: #9a9ca0;
    --rule: #8c8e92;
    --brand-grey: #bdbec0;
  }
  html, body {
    margin: 0;
    padding: 0;
    width: 1200px;
    height: 997px;
    overflow: hidden;
    background: var(--backdrop);
    font-family: "Arimo", Arial, sans-serif;
  }
  .canvas {
    position: relative;
    width: 1200px;
    height: 997px;
  }
  .card {
    position: absolute;
    width: 540px;
    height: 330px;
    background: var(--card-dark);
    box-shadow: 0 14px 30px rgba(0,0,0,.55);
    overflow: hidden;
  }
  /* Front */
  .card-front { left: 70px; top: 110px; }
  .front-band {
    position: absolute;
    left: 0; top: 0; right: 0;
    height: 150px;
    background: linear-gradient(180deg, var(--band-light) 0%, var(--band-light) 55%, var(--band-shade) 100%);
  }
  .secondary-brand {
    position: absolute;
    left: 28px; top: 104px;
    display: flex;
    align-items: center;
    gap: 8px;
    color: var(--ink-dark);
  }
  .secondary-brand .mark {
    width: 24px; height: 24px;
    border-radius: 50%;
    background: var(--ink-dark);
  }
  .secondary-brand .name {
    font-size: 14px;
    font-weight: 700;
    line-height: 1.15;
  }
  .identity {
    position: absolute;
    right: 36px; top: 96px;
    text-align: right;
    color: var(--ink-dark);
  }
  .identity .person {
    font-size: 19px;
    letter-spacing: .5px;
    text-transform: uppercase;
  }
  .identity .role {
    font-size: 13px;
    font-weight: 700;
    margin-top: 3px;
  }
  .details {
    position: absolute;
    left: 28px; right: 36px; bottom: 42px;
    color: var(--ink-light);
    text-align: right;
  }
  .details .tagline {
    font-size: 13px;
    padding-bottom: 8px;
    border-bottom: 1px solid var(--rule);
  }
  .details .contacts {
    display: flex;
    justify-content: space-between;
    font-size: 11.5px;
    color: var(--ink-muted);
    padding-top: 8px;
  }
  /* Back */
  .card-back { left: 600px; top: 520px; }
  .primary-brand {
    position: absolute;
    left: 0; right: 0; top: 0; bottom: 0;
    display: flex;
    align-items: center;
    justify-content: center;
    gap: 14px;
  }
  .primary-brand .mark {
    width: 34px; height: 34px;
    background: var(--brand-grey);
  }
  .primary-brand .name {
    font-size: 24px;
    font-weight: 400;
    letter-spacing: 2px;
    text-transform: uppercase;
    color: var(--brand-grey);
  }
</style>
</head>
<body>
<main class="canvas">
  <section class="card card-front" aria-label="Front of business card">
    <div class="front-band"></div>
    <div class="secondary-brand">
      <span class="mark"></span>
      <span class="name">Career Lantern<br>Australia</span>
    </div>
    <div class="identity">
      <div class="person">Gavin Darrow</div>
      <div class="role">Founder &amp; Director</div>
    </div>
    <div class="details">
      <div class="tagline">Recruitment &amp; employment consultant from Brisbane, Australia</div>
      <div class="contacts">
        <span>Phone: (07) 3519 6482</span>
        <span>Mobile: 0431 586 207</span>
        <span>Email: gavin@careerlantern.com.au</span>
      </div>
    </div>
  </section>

  <section class="card card-back" aria-label="Back of business card">
    <div class="primary-brand">
      <span class="mark"></span>
      <span class="name">Darrow Consulting</span>
    </div>
  </section>
</main>
</body>
</html>
```